Realtor resource

This is a website that provides resources for Realtors and their customers (home buyers and sellers).

There are 5 pages that I need redesigned:

1. Homepage: https://brightporchhelp.com/
2. Support Page/Contact Us: https://brightporchhelp.com/contact-us/
3. Agent Dashboard - See attached screenshot
4. Real Estate Documents page - See attached screenshot
5. Real Estate Contract page - see attached screenshot

Target Market(s)

Real estate agents and their customers.

Industry/Entity Type

Real Estate

Number of Pages Required

5+ page

Requirements
Must have
• Please use a modern design and incorporate design with current logo.

```html
<!DOCTYPE html>
<html lang="en">
<head>
<meta charset="utf-8">
<title>BrightPorchHelp — Real Estate Contracts Explained</title>
<link rel="stylesheet" href="https://fonts.googleapis.com/css2?family=Archivo:wght@400;500&family=Arvo&family=Lato:wght@400&family=Montserrat:wght@700&display=swap">
<style>
  :root {
    --orange: #f6921e;
    --ink: #1f1f1f;
    --nav-text: #5f5f66;
    --white: #ffffff;
    --muted: #7a7a80;
    --btn-text-dark: #4a4a52;
  }
  * { box-sizing: border-box; margin: 0; padding: 0; }
  html, body { width: 1200px; height: 796px; overflow: hidden; background: var(--white); }
  body { position: relative; font-family: "Archivo", sans-serif; }

  .site-header { position: absolute; left: 141px; top: 30px; width: 920px; height: 31px; }
  .brand { position: absolute; left: 0; top: 0; height: 31px; display: flex; align-items: center; text-decoration: none; z-index: 1; }
  .brand-name { font-family: "Archivo", sans-serif; font-weight: 500; font-size: 24px; color: var(--ink); letter-spacing: -0.3px; }

  .main-nav { position: absolute; top: 0; left: 0; width: 100%; height: 31px; }
  .nav-link { position: absolute; top: 9px; font-size: 9.6px; color: var(--nav-text); text-decoration: none; letter-spacing: 0.2px; }
  .nav-link.is-active { color: var(--orange); font-weight: 500; }
  .nav-home { left: 460px; }
  .nav-support { left: 516px; }
  .nav-docs { left: 586px; }
  .nav-dashboard { left: 726px; }

  .pill { display: inline-flex; align-items: center; justify-content: center; border-radius: 16px; font-family: "Montserrat", sans-serif; font-weight: 700; font-size: 6.6px; letter-spacing: 0.5px; text-transform: uppercase; text-decoration: none; }
  .pill-orange { background: var(--orange); color: var(--white); }
  .pill-white { background: var(--white); color: var(--btn-text-dark); }
  .get-started { position: absolute; right: 0; top: 0; width: 94px; height: 31px; }

  .hero { position: absolute; left: 141px; top: 107px; width: 920px; height: 582px; display: flex; }
  .hero-panel { position: relative; height: 100%; color: var(--white); }
  .hero-realtor { width: 459px; background: linear-gradient(180deg, #606670 0%, #77687a 40%, #9a6f78 62%, #5a3a4c 82%, #2d1a2c 100%); }
  .hero-buyers { width: 461px; background: linear-gradient(160deg, #cd7b1f 0%, #d98a34 35%, #c8803e 60%, #a06a56 85%, #8c6a70 100%); }
  .hero-content { position: absolute; left: 53px; top: 248px; }
  .hero-buyers .hero-content { left: 51px; }
  .hero-title { font-family: "Arvo", serif; font-weight: 400; font-size: 38px; line-height: 1; letter-spacing: -0.5px; white-space: nowrap; }
  .hero-text { margin-top: 20px; font-family: "Lato", sans-serif; font-size: 9.6px; line-height: 17.5px; }
  .hero-realtor .hero-text { width: 208px; }
  .hero-buyers .hero-text { width: 272px; }
  .hero-btn { position: absolute; top: 112px; left: 0; width: 94px; height: 31px; }

  .site-footer { position: absolute; right: 140px; top: 743px; font-size: 8.4px; color: var(--muted); letter-spacing: 0.2px; }
</style>
</head>
<body>
  <header class="site-header">
    <a class="brand" href="https://brightporchhelp.com/">
      <span class="brand-name">BrightPorchHelp</span>
    </a>
    <nav class="main-nav">
      <a class="nav-link nav-home is-active" href="https://brightporchhelp.com/">Home</a>
      <a class="nav-link nav-support" href="https://brightporchhelp.com/contact-us/">Support</a>
      <a class="nav-link nav-docs" href="#">Real Estate Documents</a>
      <a class="nav-link nav-dashboard" href="#">Agent Dashboard</a>
      <a class="pill pill-orange get-started" href="#">Get Started</a>
    </nav>
  </header>

  <main class="hero">
    <section class="hero-panel hero-realtor" role="img" aria-label="Row of Victorian houses at dusk behind a dark hedge">
      <div class="hero-content">
        <h2 class="hero-title">Realtor</h2>
        <p class="hero-text">Real Estat Contracts Explained in plain language by Texas real estate attorneys</p>
        <a class="pill pill-white hero-btn" href="#">Read More</a>
      </div>
    </section>
    <section class="hero-panel hero-buyers" role="img" aria-label="Hand holding a house key, wearing a leather wristwatch">
      <div class="hero-content">
        <h2 class="hero-title">Buyers &amp; Sellers</h2>
        <p class="hero-text">Lorem ipsum dolor sit amet, consectetur adipisicing elit, sed do eiusmod tempor incididunt ut.</p>
        <a class="pill pill-orange hero-btn" href="#">Read More</a>
      </div>
    </section>
  </main>

  <footer class="site-footer">© Copyright 2019, All Rights Reserved.</footer>
</body>
</html>
```